CG 1 page flyer

I need a flyer design for a financial risk advisory business. I like the layout of the example on your site, for Delia Fenwick (attached). Our business needs to show strength, safety, knowledge and security. We provide financial advice.

I have uploaded the front page of our larger brochure. I would like the man with the umbrella with the caption and the logo / brand on the front page, but with portrait orientation, instead of landscape.

For the second page (the back), I have got some ideas of the kinds of things I would want written on the attached Power Point. But it needs to be arranged better, with perhaps the Corvin's Gate Logo on there as well, to break up all the writing. Attached is an example of how it might look, but I want different formatting and layout ideas, that look better, more professional etc.

The page 1 comment what is corvins gate? predicting ......... would look better all the way along the bottom of the page, but i couldn't get the formatting right.

```html
<!DOCTYPE html>
<html lang="en">
<head>
<meta charset="utf-8">
<title>Corvin's Gate – Flyer</title>
<link href="https://fonts.googleapis.com/css2?family=Fira+Sans:ital,wght@0,300;0,400;0,600;1,300;1,400;1,600&display=swap" rel="stylesheet">
<style>
  :root {
    --navy: #232b5c;
    --sky: #3db5ea;
    --white: #ffffff;
    --paper: #ffffff;
  }
  * { margin: 0; padding: 0; box-sizing: border-box; }
  html, body { width: 887px; height: 1200px; overflow: hidden; background: var(--paper); }
  body { font-family: "Fira Sans", Arial, sans-serif; }
  .flyer { position: relative; width: 887px; height: 1200px; }
  .panel { position: absolute; left: 0; top: 0; width: 887px; height: 965px; background: var(--navy); color: var(--white); }
  .block { position: absolute; }
  .headline {
    left: 83px; top: 114px; font-weight: 300; color: var(--sky);
    font-size: 38px; line-height: 48px; letter-spacing: -0.6px;
  }
  .label {
    font-style: italic; font-weight: 600; color: var(--sky);
    font-size: 15.5px; line-height: 22px; letter-spacing: -0.2px;
  }
  .label-title { font-size: 17px; letter-spacing: -0.3px; }
  .copy { font-weight: 300; font-size: 16.2px; line-height: 23.8px; letter-spacing: -0.1px; }
  .left { left: 84px; width: 345px; }
  .right { left: 461px; width: 345px; }
  .services { list-style: none; margin-top: 4px; }
  .services li {
    position: relative; padding-left: 23px; font-weight: 600;
    font-size: 16.2px; line-height: 24.7px; letter-spacing: -0.2px;
  }
  .services li::before {
    content: ""; position: absolute; left: 1px; top: 6px;
    border-left: 8px solid var(--sky); border-top: 6.5px solid transparent; border-bottom: 6.5px solid transparent;
  }
  .strapline {
    position: absolute; left: 96px; top: 1002px; color: var(--navy);
    font-style: italic; font-weight: 300; font-size: 29px; line-height: 42px; letter-spacing: -0.4px;
  }
  .brand { position: absolute; left: 514px; top: 1000px; width: 310px; }
  .brand-mark { position: absolute; left: 226px; top: 6px; }
  .brand-name {
    position: absolute; left: 0; top: 58px; white-space: nowrap;
    color: var(--navy); font-weight: 600; font-size: 45px; line-height: 56px; letter-spacing: -1px;
  }
  .brand-tagline {
    position: absolute; left: 1px; top: 124px; white-space: nowrap;
    color: var(--sky); font-size: 15px; line-height: 18px; word-spacing: 2px;
  }
</style>
</head>
<body>
<main class="flyer">
  <section class="panel">
    <h1 class="block headline">You can’t Outsource<br>your Risk,<br>but you can<br>Insource Expertise</h1>

    <div class="block left" style="top:336px">
      <h2 class="label label-title">WHO&nbsp; IS&nbsp; CORVIN’S GATE?</h2>
      <p class="copy">A team of independent, passionate risk advisors with over 200 years combined experience in financial market risk management, funding &amp; debt advisory.</p>
    </div>

    <div class="block left" style="top:478px">
      <h2 class="label">WHAT&nbsp; CAN WE DO FOR&nbsp; YOU?</h2>
      <p class="copy">We partner with clients to gain a deep understanding of their needs. We then help them solve their risk and funding issues by creating and explaining sustainable treasury policy.</p>
    </div>

    <div class="block left" style="top:639px">
      <h2 class="label label-title">Debt Advisory</h2>
      <p class="copy">Design &amp; Execution of&nbsp; debt funding strategies.<br>Market Risk Advisory<br>Design &amp; Execution of&nbsp; hedging strategies<br>Active Engagement<br>Fully engaged risk review, reporting, strategy development&nbsp; and execution enhancement.</p>
    </div>

    <div class="block left" style="top:825px">
      <h2 class="label">WHAT IS OUR MEASURE OF SUCCESS?</h2>
      <p class="copy">Our only true measure of success is successful, sustainable clients that stand out from their peers.</p>
    </div>

    <div class="block right" style="top:167px">
      <h2 class="label">WHAT IT MEANS FOR OUR CLIENTS</h2>
      <p class="copy">Our market experience means our clients receive well considered, completely independent advice and solutions&nbsp; covering:</p>
      <ul class="services">
        <li>Commodities</li>
        <li>Foreign Exchange</li>
        <li>Interest Rates</li>
        <li>Project Finance</li>
        <li>Treasury Software Solutions</li>
        <li>Market Valuations incl. CVA / DVA</li>
        <li>Hedge Effectiveness Testing</li>
        <li>Compliance Reporting</li>
      </ul>
    </div>

    <div class="block right" style="top:487px">
      <h2 class="label">OUR PRINCIPLES</h2>
      <p class="copy">Aspire to always deliver value to our clients.<br>Always provide frank, robust advice.<br>Be fierce but commercial client advocates.</p>
    </div>

    <div class="block right" style="top:610px">
      <h2 class="label">WHAT’S OUR PHILOSOPHY?</h2>
      <p class="copy">Markets are dynamic, so proper Risk Management must also be a dynamic and on-going process. Risk Management is not about “beating the market”, its about “not taking a beating” from adverse market conditions.</p>
      <p class="copy" style="margin-top:24px">When your bottom line is exposed to volatile markets, appropriate preparation is the key to a sustainable business. We help our clients to integrate their risk management objectives with their overall corporate strategy.</p>
    </div>
  </section>

  <p class="strapline">Integration of Market<br>Risk Strategy &amp; Corporate<br>Strategy is Essential</p>

  <div class="brand">
    <svg class="brand-mark" width="48" height="48" viewBox="0 0 48 48" aria-hidden="true">
      <circle cx="24" cy="24" r="22" fill="#232b5c"/>
    </svg>
    <div class="brand-name">Corvin’s Gate</div>
    <div class="brand-tagline">Our experience&nbsp;&nbsp; Your edge</div>
  </div>
</main>
</body>
</html>
```